Redesign Craft Brewing Recipe Website

Originally built with Bootstrap just to get the site going, I am seeking a complete redesign of the sites home page and recipe page. I am an experienced web developer with no graphic background, initially just looking for psd mocks.

I prefer styles that are clean and modern, and would prefer anything that is fun, engaging, and has an organic feel to it. I currently have a cartoon rabbit as a logo, but it needs some modification/tweaking, so any help in that area would be great as well.

Current site:
http://kettlewren.plumhostsite.net/

Current launch page/logo:
http://www.kettlewren.com/

I like the overall layout of the elements currently, but the design sucks.

The launch page is at the following URL

Reason: Still looking for a more modern design. Designs received so far are too similar to the original.

My site is content based and does not contain images or products. Your design should not consist of large images.

Reason: The website has very little images, so the designs need to be more text and content based. The header needs to be very small and should not contain an ad rotater.

Target Market(s)

Home brewers, Craft brewers, Microbreweries, Brewpubs

Requirements
Must have
• Web 2.0 Look and Feel, Fun, Hip, Focus on content
Should not have
• A large photo as a header

```html
<!DOCTYPE html>
<html lang="en">
<head>
<meta charset="utf-8">
<title>Kettlewren – Latest Recipes</title>
<link href="https://fonts.googleapis.com/css2?family=Signika:wght@400;600&family=Roboto+Condensed:wght@400;700&family=Open+Sans:wght@400;600&display=swap" rel="stylesheet">
<style>
  :root {
    --page-bg: #eeece8;
    --header-bg: #4a4646;
    --header-bg-dark: #403c3c;
    --brand-blue: #2a9fd0;
    --tag-red: #d64848;
    --tag-blue: #2fa4d2;
    --stat-grey: #575555;
    --ink: #3a3a3a;
    --ink-soft: #9a9a9a;
    --panel: #fbfbfb;
    --line: #e3e1dd;
    --white: #ffffff;
    --black: #0d0d0d;
  }
  * { box-sizing: border-box; margin: 0; padding: 0; }
  html, body { width: 950px; height: 1200px; overflow: hidden; }
  body {
    position: relative;
    background: var(--page-bg);
    font-family: "Open Sans", sans-serif;
    color: var(--ink);
  }

  /* Header */
  .site-header {
    position: absolute; left: 0; top: 0; width: 950px; height: 94px;
    background: linear-gradient(180deg, var(--header-bg) 0%, var(--header-bg-dark) 100%);
  }
  .brand { position: absolute; left: 100px; top: 18px; display: flex; align-items: center; }
  .brand-mark { width: 40px; height: 40px; border-radius: 50%; background: var(--white); margin-right: 10px; }
  .brand-name {
    font-family: "Signika", sans-serif; font-weight: 600; font-size: 32px;
    color: var(--brand-blue); line-height: 1;
  }
  .brand-tagline {
    position: absolute; left: 184px; top: 55px; width: 160px;
    font-size: 9.5px; line-height: 11px; color: var(--white);
  }
  .main-nav { position: absolute; right: 102px; top: 42px; display: flex; gap: 24px; }
  .main-nav a {
    position: relative; font-family: "Open Sans", sans-serif; font-size: 11px;
    color: var(--white); text-decoration: none; text-transform: uppercase; letter-spacing: .1px;
  }
  .main-nav a.is-active::after {
    content: ""; position: absolute; left: -5px; right: -5px; top: 38px; height: 4px;
    background: var(--brand-blue);
  }

  /* Sidebar */
  .search-panel {
    position: absolute; left: 94px; top: 115px; width: 238px; height: 1036px;
    background: var(--panel); border: 1px solid var(--line);
  }
  .filter-title {
    position: absolute; left: 20px; font-family: "Roboto Condensed", sans-serif;
    font-weight: 700; font-size: 19px; color: #333;
  }
  .filter-title span { color: var(--brand-blue); }
  .field {
    position: absolute; left: 15px; width: 208px; height: 32px;
    background: var(--white); border: 1px solid var(--line);
    font-size: 11px; color: #555; padding: 0 17px; display: flex; align-items: center; justify-content: space-between;
  }
  .field.is-placeholder { color: #aaa; font-size: 12px; }
  .field.is-dark { font-family: "Roboto Condensed", sans-serif; font-size: 12px; color: #444; }
  .range-label { position: absolute; left: 22px; top: 351px; font-family: "Roboto Condensed", sans-serif; font-size: 10.5px; color: #444; }
  .range { position: absolute; left: 18px; top: 365px; width: 202px; height: 40px; }
  .range-button {
    position: absolute; left: 3px; top: 424px; width: 230px; height: 25px;
    background: linear-gradient(180deg, #4a4a4a, #151515); border-radius: 2px;
    color: var(--white); font-family: "Roboto Condensed", sans-serif; font-weight: 700;
    font-size: 11.5px; text-transform: uppercase; display: flex; align-items: center; justify-content: center;
  }

  /* Recipe list */
  .recipes {
    position: absolute; left: 347px; top: 116px; width: 510px; height: 1035px;
    background: var(--panel); border: 1px solid var(--line);
  }
  .recipes-title {
    position: absolute; left: 14px; top: 19px; font-family: "Signika", sans-serif;
    font-weight: 600; font-size: 33px; color: #4a4a4a; letter-spacing: -.5px;
  }
  .recipes-title span { color: var(--brand-blue); }
  .sort-tabs { position: absolute; left: 16px; top: 66px; font-size: 12px; color: #333; }
  .sort-tabs .is-active { color: var(--tag-red); }
  .sort-tabs .sep { margin: 0 8px; }
  .recipe-list { position: absolute; left: 0; top: 97px; width: 508px; border-top: 1px solid var(--line); list-style: none; }
  .recipe {
    position: relative; height: 148px; border-bottom: 1px solid var(--line);
  }
  .recipe:last-child { border-bottom: none; }
  .recipe-photo {
    position: absolute; left: 15px; top: 18px; width: 74px; height: 77px;
    border: 1px solid var(--line);
    background: linear-gradient(90deg, #fff 0%, #5b5a2a 25%, #a32a30 50%, #1d1b1d 75%, #fff 100%);
  }
  .recipe-name {
    position: absolute; left: 96px; top: 17px; font-family: "Roboto Condensed", sans-serif;
    font-weight: 400; font-size: 17.5px; color: #3a3a3a;
  }
  .recipe-author { position: absolute; left: 97px; top: 42px; font-family: "Roboto Condensed", sans-serif; font-size: 9.5px; color: var(--ink-soft); }
  .recipe-author b { font-weight: 400; color: #333; }
  .recipe-summary { position: absolute; left: 97px; top: 59px; width: 400px; font-size: 10px; line-height: 14.5px; color: var(--ink-soft); }
  .recipe-tags { position: absolute; left: 97px; top: 99px; display: flex; gap: 7px; height: 25px; }
  .tag {
    display: flex; align-items: center; justify-content: center; color: var(--white);
    font-family: "Roboto Condensed", sans-serif; font-weight: 700; font-size: 13px; height: 25px;
  }
  .tag-method { width: 65px; background: var(--tag-red); }
  .tag-style { width: 80px; background: var(--tag-blue); }
  .tag-style.is-long { font-size: 10px; }
  .stats { display: flex; width: 238px; background: var(--stat-grey); padding: 0 6px; }
  .stat {
    flex: 1; display: flex; flex-direction: column; align-items: center; justify-content: center;
    color: var(--white); font-family: "Open Sans", sans-serif; font-weight: 600; font-size: 8.5px; line-height: 9.5px;
  }

  .results-bar {
    position: absolute; left: -1px; bottom: -1px; width: 510px; height: 43px; background: var(--black);
    color: var(--white); font-family: "Roboto Condensed", sans-serif; font-weight: 700; font-size: 12px;
  }
  .results-bar .label { position: absolute; left: 22px; top: 14px; }
  .results-bar .count { position: absolute; left: 122px; top: 14px; }
  .pager { position: absolute; right: 19px; top: 12px; display: flex; gap: 8px; }
  .pager span {
    width: 38px; height: 19px; background: var(--white); color: #333; font-size: 10.5px;
    display: flex; align-items: center; justify-content: center; border-radius: 1px;
  }

  .site-footer { position: absolute; left: 109px; top: 1167px; font-family: "Roboto Condensed", sans-serif; font-size: 10.5px; color: #444; }
</style>
</head>
<body>
  <header class="site-header">
    <div class="brand"><span class="brand-mark"></span><span class="brand-name">Kettlewren</span></div>
    <p class="brand-tagline">Easiest way to create and share craft beer recipes.</p>
    <nav class="main-nav">
      <a class="is-active" href="#">Home</a>
      <a href="#">Recipes</a>
      <a href="#">About Us</a>
      <a href="#">Our Clients</a>
      <a href="#">Contact</a>
    </nav>
  </header>

  <aside class="search-panel">
    <h2 class="filter-title" style="top:29px">Search <span>Recipes</span></h2>
    <div class="field is-placeholder" style="top:53px">Stout</div>
    <h2 class="filter-title" style="top:114px">Match Maker</h2>
    <div class="field is-dark" style="top:138px">Boil Size
      <svg width="8" height="8" viewBox="0 0 8 8"><circle cx="4" cy="4" r="3.4" fill="none" stroke="#bbb"/><circle cx="4" cy="4" r="1.6" fill="#333"/></svg>
    </div>
    <h2 class="filter-title" style="top:190px">Brewing</h2>
    <div class="field" style="top:214px">Extract
      <svg width="8" height="6" viewBox="0 0 8 6"><path d="M0 0h8L4 6z" fill="#555"/></svg>
    </div>
    <h2 class="filter-title" style="top:266px">Styles</h2>
    <div class="field" style="top:289px">American Amber Ale
      <svg width="8" height="6" viewBox="0 0 8 6"><path d="M0 0h8L4 6z" fill="#555"/></svg>
    </div>
    <p class="range-label">0 Gals to 25 Gals</p>
    <svg class="range" viewBox="0 0 202 40">
      <rect x="0" y="6" width="202" height="6" rx="3" fill="#e4e4e4" stroke="#ccc" stroke-width=".6"/>
      <rect x="48" y="6" width="108" height="6" fill="#7cbde9"/>
      <path d="M43 3h9v7l-4.5 4-4.5-4z" fill="#f4f4f4" stroke="#999" stroke-width=".7"/>
      <path d="M152 3h9v7l-4.5 4-4.5-4z" fill="#f4f4f4" stroke="#999" stroke-width=".7"/>
      <g stroke="#888" stroke-width=".6">
        <line x1="7" y1="16" x2="7" y2="20"/><line x1="48" y1="16" x2="48" y2="20"/><line x1="106" y1="16" x2="106" y2="20"/><line x1="156" y1="16" x2="156" y2="20"/><line x1="196" y1="16" x2="196" y2="20"/>
      </g>
      <g font-family="Open Sans, sans-serif" font-size="7" font-weight="600" fill="#444" text-anchor="middle">
        <text x="7" y="30">5</text><text x="48" y="30">10</text><text x="106" y="30">15</text><text x="156" y="30">20</text><text x="196" y="30">25</text>
      </g>
    </svg>
    <div class="range-button">Update Search</div>
  </aside>

  <main class="recipes">
    <h1 class="recipes-title">Latest <span>Recipes</span></h1>
    <p class="sort-tabs"><span class="is-active">Popular</span><span class="sep">/</span>Recent</p>
    <ul class="recipe-list">
      <li class="recipe">
        <div class="recipe-photo" role="img" aria-label="Photo of three recipe bottles"></div>
        <h3 class="recipe-name">Old Fence Sweet Mead</h3>
        <p class="recipe-author">Created by <b>Dana Whitlock</b></p>
        <p class="recipe-summary">Le Lorem Ipsum est simplement du faux texte employé dans la composition mise en page avant impression.</p>
        <div class="recipe-tags"><span class="tag tag-method">Extract</span><span class="tag tag-style">Sweet Mead</span>
          <div class="stats"><span class="stat">2.24%<span>abv</span></span><span class="stat">24<span>ibu</span></span><span class="stat">1.006<span>fb</span></span><span class="stat">1.022<span>og</span></span><span class="stat">9<span>SRM</span></span></div></div>
      </li>
      <li class="recipe">
        <div class="recipe-photo" role="img" aria-label="Photo of two recipe bottles"></div>
        <h3 class="recipe-name">Night Owl Sweet Stout</h3>
        <p class="recipe-author">Created by <b>Dana Whitlock</b></p>
        <p class="recipe-summary">Le Lorem Ipsum est simplement du faux texte employé dans la composition mise en page avant impression.</p>
        <div class="recipe-tags"><span class="tag tag-method">Extract</span><span class="tag tag-style">Sweet Stout</span>
          <div class="stats"><span class="stat">2.24%<span>abv</span></span><span class="stat">24<span>ibu</span></span><span class="stat">1.006<span>fb</span></span><span class="stat">1.022<span>og</span></span><span class="stat">9<span>SRM</span></span></div></div>
      </li>
      <li class="recipe">
        <div class="recipe-photo" role="img" aria-label="Photo of three recipe bottles"></div>
        <h3 class="recipe-name">Meadowgold Traditional Bock</h3>
        <p class="recipe-author">Created by <b>Dana Whitlock</b></p>
        <p class="recipe-summary">Le Lorem Ipsum est simplement du faux texte employé dans la composition mise en page avant impression.</p>
        <div class="recipe-tags"><span class="tag tag-method">Extract</span><span class="tag tag-style is-long">Traditional Bock</span>
          <div class="stats"><span class="stat">2.24%<span>abv</span></span><span class="stat">24<span>ibu</span></span><span class="stat">1.006<span>fb</span></span><span class="stat">1.022<span>og</span></span><span class="stat">9<span>SRM</span></span></div></div>
      </li>
      <li class="recipe">
        <div class="recipe-photo" role="img" aria-label="Photo of three recipe bottles"></div>
        <h3 class="recipe-name">Riverbend Dunkelweizen</h3>
        <p class="recipe-author">Created by <b>Dana Whitlock</b></p>
        <p class="recipe-summary">Le Lorem Ipsum est simplement du faux texte employé dans la composition mise en page avant impression.</p>
        <div class="recipe-tags"><span class="tag tag-method">Extract</span><span class="tag tag-style">Dunkelweizen</span>
          <div class="stats"><span class="stat">2.24%<span>abv</span></span><span class="stat">24<span>ibu</span></span><span class="stat">1.006<span>fb</span></span><span class="stat">1.022<span>og</span></span><span class="stat">9<span>SRM</span></span></div></div>
      </li>
      <li class="recipe">
        <div class="recipe-photo" role="img" aria-label="Photo of two recipe bottles"></div>
        <h3 class="recipe-name">Ironwood Baltic Porter</h3>
        <p class="recipe-author">Created by <b>Dana Whitlock</b></p>
        <p class="recipe-summary">Le Lorem Ipsum est simplement du faux texte employé dans la composition mise en page avant impression.</p>
        <div class="recipe-tags"><span class="tag tag-method">Extract</span><span class="tag tag-style">Dunkelweizen</span>
          <div class="stats"><span class="stat">2.24%<span>abv</span></span><span class="stat">24<span>ibu</span></span><span class="stat">1.006<span>fb</span></span><span class="stat">1.022<span>og</span></span><span class="stat">9<span>SRM</span></span></div></div>
      </li>
      <li class="recipe">
        <div class="recipe-photo" role="img" aria-label="Photo of two recipe bottles"></div>
        <h3 class="recipe-name">Riverbend Munich Helles</h3>
        <p class="recipe-author">Created by <b>Dana Whitlock</b></p>
        <p class="recipe-summary">Le Lorem Ipsum est simplement du faux texte employé dans la composition mise en page avant impression.</p>
        <div class="recipe-tags"><span class="tag tag-method">Extract</span><span class="tag tag-style">Dunkelweizen</span>
          <div class="stats"><span class="stat">2.24%<span>abv</span></span><span class="stat">24<span>ibu</span></span><span class="stat">1.006<span>fb</span></span><span class="stat">1.022<span>og</span></span><span class="stat">9<span>SRM</span></span></div></div>
      </li>
    </ul>
    <div class="results-bar">
      <span class="label">Search Result</span>
      <span class="count">12 Found</span>
      <div class="pager"><span>Prev</span><span>Next</span></div>
    </div>
  </main>

  <footer class="site-footer">Copyright 2013 Website Name. All Rights Reserved.</footer>
</body>
</html>
```